Borrowed Lanterns - the new thriller in the Tidewater series by award-winning author Marta K. Belloway

Looking for an book cover design for the 4th book in the Tidewater series by Marta K. Belloway. Covers from the first 3 books are attached. Would like to keep a series look going, so possibly using a hand holding a paint brush might work - but not tied down to showing a hand on the cover. Most of the book takes place in a rustic Arizona desert estate in a national forest - so something depicting a desert scene might work too. The cover needs to convey a "thriller" feeling. Attached is our design template with needed specs. Also attached are two other covers for inspiration:

A GARDEN UNDER SALT - something like this could work in the key were a paintbrush and the scene is set in the Arizona desert

THE ORCHARD AT NOON - this could work too with Arizona desert setting

Here's the synopsis of BORROWED LANTERNS:

Her life ended and she is disappointed to discover she is still alive.

With all ties to her handler or anyone connected to her life as a hired killer, she struggles to understand who and even what she has become. She knows she doesn’t want to kill again. And yes, danger finds her and she responds, animal-like, in the only way she knows how.

In this mood of absolute bereavement, she comes across Harriet Vasquell, a world famous artist who has spent the last three decades living a hermit-like existence on a rustic desert estate in a national forest.

Harriet invites her to stay on to assist the old woman who will, in return, mentor our narrator as she deepens her own interest in art.

What is not at first apparent is that elements of Harriet’s past are shrouded in danger, sorrow and darkness and rather than growing as an artist, she soon finds herself enmeshed in a dangerous mystery with strands that stretch decades into the past.

```html
<!DOCTYPE html>
<html lang="en">
<head>
<meta charset="utf-8">
<title>Borrowed Lanterns — Marta K. Belloway</title>
<link rel="stylesheet" href="https://fonts.googleapis.com/css2?family=Bebas+Neue&family=Oswald:wght@500&display=swap">
<style>
  :root {
    --ink-night: #05070c;
    --sky-deep: #0a1326;
    --sky-mid: #1c3a6e;
    --sky-glow: #5d94d6;
    --sky-haze: #b9d6f4;
    --horizon: #5a6196;
    --dune-lilac: #4b4f80;
    --dune-mid: #2c3058;
    --dune-shadow: #15182e;
    --title-red: #c8161d;
    --title-white: #f6f8fc;
    --author-white: #eef0f3;
  }
  html, body {
    margin: 0;
    padding: 0;
    width: 811px;
    height: 1200px;
    overflow: hidden;
    background: var(--ink-night);
  }
  .cover {
    position: relative;
    width: 811px;
    height: 1200px;
    overflow: hidden;
    background: var(--ink-night);
  }
  .cover__scene {
    position: absolute;
    inset: 0;
    background:
      radial-gradient(ellipse 40% 26% at 52% 40%, rgba(185,214,244,0.55), rgba(93,148,214,0.25) 50%, rgba(10,19,38,0) 100%),
      radial-gradient(ellipse 75% 9% at 62% 60%, rgba(122,128,186,0.75), rgba(90,97,150,0) 100%),
      radial-gradient(ellipse 60% 10% at 25% 70%, rgba(96,100,150,0.55), rgba(75,79,128,0) 100%),
      radial-gradient(ellipse 70% 12% at 70% 80%, rgba(70,74,120,0.5), rgba(44,48,88,0) 100%),
      radial-gradient(ellipse 90% 30% at 50% 100%, rgba(5,7,12,0.9), rgba(5,7,12,0) 100%),
      linear-gradient(180deg,
        var(--ink-night) 0%,
        var(--ink-night) 10%,
        var(--sky-deep) 18%,
        var(--sky-mid) 36%,
        #2d5594 48%,
        var(--horizon) 57%,
        var(--dune-lilac) 62%,
        var(--dune-mid) 72%,
        var(--dune-shadow) 86%,
        var(--ink-night) 100%);
  }
  .cover__type {
    position: absolute;
    inset: 0;
    width: 811px;
    height: 1200px;
  }
  .title-top,
  .title-main {
    font-family: "Bebas Neue", sans-serif;
  }
  .title-top { fill: var(--title-red); }
  .author {
    font-family: "Oswald", sans-serif;
    font-weight: 500;
    fill: var(--author-white);
  }
</style>
</head>
<body>
  <main class="cover">
    <div class="cover__scene" role="img" aria-label="Starry blue night sky glowing above moonlit rolling desert dunes"></div>

    <svg class="cover__type" viewBox="0 0 811 1200" aria-label="Borrowed Lanterns by Marta K. Belloway">
      <defs>
        <linearGradient id="title-fade" gradientUnits="userSpaceOnUse" x1="0" y1="170" x2="0" y2="662">
          <stop offset="0" stop-color="var(--title-white)" stop-opacity="1"/>
          <stop offset="0.35" stop-color="var(--sky-haze)" stop-opacity="0.9"/>
          <stop offset="0.7" stop-color="var(--sky-glow)" stop-opacity="0.55"/>
          <stop offset="1" stop-color="var(--horizon)" stop-opacity="0.15"/>
        </linearGradient>
      </defs>

      <text class="title-top" x="405" y="157" text-anchor="middle" font-size="205"
            textLength="730" lengthAdjust="spacingAndGlyphs">BORROWED</text>

      <text class="title-main" x="405" y="662" text-anchor="middle" font-size="700"
            textLength="690" lengthAdjust="spacingAndGlyphs" fill="url(#title-fade)">LANTERNS</text>

      <text class="author" x="405" y="1143" text-anchor="middle" font-size="84"
            textLength="595" lengthAdjust="spacingAndGlyphs">MARTA K. BELLOWAY</text>
    </svg>
  </main>
</body>
</html>
```